Security and Automation Company based in Texas and needs logo design also

Looking for a new logo design for our company - we are based in Texas and specialize in camera, security and home automation - We do want the main company name(Brightline Guard and Controls of Texas) with our parent company in small letters below (a Veloran Partners, LLC Company) and our License number needs to be included in the design - K74836 - Darker shades of blue preferred

Target Market(s)

We work with everyone from home to large corporate - so clean design would be helpful

Industry/Entity Type

It Company

Contact Information for Business Card

PO Box 4719
Cedar Hollow, Texas 75961
Leave a spot for the phone number and email address

Logo Text

Brightline Guard and Controls of Texas/a Veloran Partners Company/K74836

Font styles to use
Sans Serif

Colors
0255a3

```html
<!DOCTYPE html>
<html lang="en">
<head>
<meta charset="utf-8">
<title>Brightline Guard and Controls of Texas Business Card</title>
<link rel="stylesheet" href="https://fonts.googleapis.com/css2?family=Lato:wght@400;700;900&display=swap">
<style>
  :root {
    --backdrop: #545454;
    --card-white: #ffffff;
    --brand-blue: #0255a3;
    --brand-blue-deep: #023f7a;
    --brand-blue-soft: #0a62b5;
    --ink: #1e1e1e;
    --band-dark: #232323;
    --rule: #8a8a8a;
    --on-dark: #ffffff;
  }
  * { margin: 0; padding: 0; box-sizing: border-box; }
  html, body { width: 1200px; height: 900px; overflow: hidden; }
  body {
    background: var(--backdrop);
    position: relative;
    font-family: "Lato", Arial, sans-serif;
    color: var(--ink);
  }
  .card {
    position: absolute;
    top: 170px;
    width: 347px;
    height: 561px;
    box-shadow: 3px 4px 8px rgba(0,0,0,0.45);
    overflow: hidden;
  }
  .card-front { left: 259px; background: var(--card-white); }
  .card-back { left: 631px; background: var(--brand-blue-deep); }

  .brand-mark {
    position: absolute;
    left: 50%;
    top: 82px;
    width: 60px;
    height: 60px;
    margin-left: -30px;
    border-radius: 50%;
    background: var(--brand-blue);
  }
  .brand-name {
    position: absolute;
    top: 152px;
    left: 20px;
    right: 20px;
    text-align: center;
    font-weight: 700;
    font-size: 19px;
    line-height: 23px;
    color: var(--brand-blue);
  }
  .brand-parent {
    position: absolute;
    top: 204px;
    left: 30px;
    right: 30px;
    display: flex;
    align-items: center;
    gap: 8px;
    font-size: 12px;
    letter-spacing: 0.4px;
    color: var(--ink);
    white-space: nowrap;
  }
  .brand-parent::before, .brand-parent::after {
    content: "";
    flex: 1;
    height: 1px;
    background: var(--rule);
  }

  .contact {
    position: absolute;
    top: 288px;
    width: 100%;
    text-align: center;
  }
  .person-name {
    font-size: 21px;
    line-height: 26px;
    font-weight: 400;
    color: var(--ink);
  }
  .person-name .first { color: var(--brand-blue); }
  .person-role { font-size: 15px; line-height: 20px; }
  .divider {
    width: 135px;
    height: 1px;
    background: var(--rule);
    margin: 11px auto;
  }
  .contact-line { font-size: 15.5px; line-height: 20.5px; }

  .license-band {
    position: absolute;
    top: 478px;
    left: 0;
    width: 100%;
    height: 58px;
    background: var(--band-dark);
    color: var(--on-dark);
    font-size: 15.5px;
    display: flex;
    align-items: center;
    justify-content: center;
  }

  .back-field {
    position: absolute;
    inset: 0 0 94px 0;
    background: linear-gradient(180deg, var(--brand-blue-deep) 0%, var(--brand-blue) 45%, var(--brand-blue-deep) 100%);
  }
  .back-mark {
    position: absolute;
    left: 50%;
    top: 200px;
    width: 120px;
    height: 120px;
    margin-left: -60px;
    border-radius: 50%;
    background: var(--on-dark);
  }
  .service-band {
    position: absolute;
    top: 467px;
    left: 0;
    width: 100%;
    height: 66px;
    background: var(--band-dark);
    color: var(--on-dark);
    font-size: 15.5px;
    line-height: 20px;
    text-transform: uppercase;
    text-align: center;
    display: flex;
    flex-direction: column;
    justify-content: center;
    letter-spacing: 0.3px;
  }
</style>
</head>
<body>
  <section class="card card-front">
    <div class="brand-mark"></div>
    <div class="brand-name">Brightline Guard and Controls<br>of Texas</div>
    <div class="brand-parent">a Veloran Partners, LLC Company</div>

    <div class="contact">
      <div class="person-name"><span class="first">Daniel</span> Harper</div>
      <div class="person-role">Managing Director</div>
      <div class="divider"></div>
      <div class="contact-line">444 555 7290</div>
      <div class="contact-line">info@veloranpartners.com</div>
      <div class="divider"></div>
      <div class="contact-line">PO Box 4719</div>
      <div class="contact-line">Cedar Hollow, Texas 75961</div>
    </div>

    <div class="license-band">Licence No. K74836</div>
  </section>

  <section class="card card-back">
    <div class="back-field"></div>
    <div class="back-mark"></div>
    <div class="service-band">
      <span>Specialize in camera</span>
      <span>security &amp; home automation</span>
    </div>
  </section>
</body>
</html>
```